Hispanic Financial Counseling and Advocate Firm seeks business card design

Looking for a clean, professional business card design. This is a firm that specializes in providing financial education, coaching, and planning to the Hispanic community. The name of the company is Valemar, which means to prosper. We need a design that is clean, professional, and invokes trust, professionalism, but also welcoming. Our logo is a plant growing from a hand to give the messaging of of being in control of growing your financial future and security. Its part of a larger organization names Celesta Financial Group, who's logo is a tree with multi colored branches. We have the back of the card designed so we just need the front designed. the back is blue, so front needs to be a different background color, not blue.

Target Market(s)

Hispanic Community looking to better their future

Industry/Entity Type

financial services

Contact Information for Business Card

contact info: Anselmo Ibarra Jr, 951-555-0147, info@celestafinancialgroup.example. Celestafinancialgroup.example. tag line: Para un futuro mas seguro!

Requirements
Must have
• basics: logo, contact info.
Nice to have
• possibly incorporate the tree logo provided somehow
Should not have
• should not look like the back, needs to be different from the back provided.

```html
<!DOCTYPE html>
<html lang="es">
<head>
<meta charset="utf-8">
<title>Valemar – Business Cards</title>
<link rel="stylesheet" href="https://fonts.googleapis.com/css2?family=Arimo:wght@400;700&display=swap">
<style>
  :root {
    --bg: #e4e5e7;
    --card: #ffffff;
    --navy: #0b3550;
    --back-navy: #053046;
    --slate: #3f4a6a;
    --green: #5e9f3a;
    --leaf-green: #8cc63f;
    --leaf-red: #e8464f;
    --leaf-blue: #27a3dd;
    --leaf-purple: #a48bc6;
    --leaf-yellow: #f2c121;
    --text: #1d1d1f;
    --white: #ffffff;
  }
  * { margin: 0; padding: 0; box-sizing: border-box; }
  html, body {
    width: 1200px; height: 1021px; overflow: hidden;
    background: var(--bg);
    font-family: "Arimo", Arial, sans-serif;
  }

  /* ---------- Back card ---------- */
  .card-back {
    position: absolute; left: 420px; top: 40px;
    width: 640px; height: 366px;
    background: var(--back-navy);
    box-shadow: 0 6px 18px rgba(0,0,0,0.22);
    overflow: hidden;
  }
  .back-tree {
    position: absolute; left: 120px; top: 60px;
    width: 150px; height: 150px;
  }
  .back-divider {
    position: absolute; left: 305px; top: 55px;
    width: 2px; height: 165px; background: var(--white);
  }
  .back-name {
    position: absolute; left: 330px; top: 95px;
    color: var(--white); font-weight: 700; line-height: 1;
  }
  .back-name .line-main { display: block; font-size: 58px; letter-spacing: -1px; }
  .back-name .line-sub { display: block; font-size: 22px; margin-top: 8px; letter-spacing: 1.5px; }
  .services {
    position: absolute; left: 0; right: 0; top: 250px;
    text-align: center; color: var(--white);
    font-size: 17px; line-height: 23px; letter-spacing: 0.5px;
  }
  .services .row { display: block; }
  .services .item { display: inline-flex; align-items: center; gap: 5px; margin: 0 6px; }
  .services .dot { width: 8px; height: 11px; border-radius: 50% 50% 50% 50% / 60% 60% 40% 40%; display: inline-block; }
  .dot.green { background: var(--leaf-green); }
  .dot.blue { background: var(--leaf-blue); }
  .dot.red { background: var(--leaf-red); }
  .dot.purple { background: var(--leaf-purple); }
  .dot.yellow { background: var(--leaf-yellow); }

  /* ---------- Front card ---------- */
  .card-front {
    position: absolute; left: 120px; top: 440px;
    width: 1000px; height: 571px;
    transform: scale(0.96); transform-origin: top left;
    background: var(--card);
    box-shadow: 0 6px 18px rgba(0,0,0,0.18);
    overflow: hidden;
  }
  .card-art { position: absolute; inset: 0; }
  .brand {
    position: absolute; left: 150px; top: 95px;
    display: flex; align-items: center; gap: 14px;
  }
  .brand-dot { width: 34px; height: 34px; border-radius: 50%; background: var(--green); }
  .brand-name { font-size: 54px; font-weight: 700; color: var(--green); letter-spacing: -0.5px; }
  .holder {
    position: absolute; left: 120px; top: 205px;
    font-size: 31px; font-weight: 700; color: var(--slate); letter-spacing: 0.5px;
  }
  .holder .suffix { color: var(--green); }
  .contact-list {
    position: absolute; left: 100px; top: 275px;
    list-style: none; font-size: 22px; color: var(--text); line-height: 31px;
  }
  .contact-list li { display: flex; align-items: center; gap: 8px; }
  .contact-list svg { width: 18px; height: 18px; flex: none; }
</style>
</head>
<body>
  <!-- Back of card -->
  <div class="card-back">
    <svg class="back-tree" viewBox="0 0 150 150" width="150" height="150">
      <defs>
        <radialGradient id="backCanopy" cx="50%" cy="40%" r="60%">
          <stop offset="0%" stop-color="#27a3dd"/>
          <stop offset="40%" stop-color="#8cc63f"/>
          <stop offset="70%" stop-color="#a48bc6"/>
          <stop offset="100%" stop-color="#053046" stop-opacity="0"/>
        </radialGradient>
      </defs>
      <rect x="0" y="0" width="150" height="150" rx="70" fill="url(#backCanopy)" opacity="0.7"
            role="img" aria-label="Multicoloured tree growing from a white open hand above a small hill"/>
    </svg>
    <div class="back-divider"></div>
    <div class="back-name">
      <span class="line-main">Celesta</span>
      <span class="line-sub">Financial Group Inc</span>
    </div>
    <div class="services">
      <span class="row">
        <span class="item"><span class="dot green"></span>Inmigración</span>
        <span class="item"><span class="dot blue"></span>Planificacion Financiera</span>
      </span>
      <span class="row">
        <span class="item"><span class="dot red"></span>Seguros</span>
        <span class="item"><span class="dot purple"></span>Impuestos</span>
        <span class="item"><span class="dot red"></span>Y mas</span>
      </span>
      <span class="row">
        <span class="item"><span class="dot yellow"></span>Preparación de documentos</span>
      </span>
    </div>
  </div>

  <!-- Front of card -->
  <div class="card-front">
    <svg class="card-art" viewBox="0 0 1000 571" width="1000" height="571">
      <defs>
        <radialGradient id="canopy" cx="50%" cy="45%" r="60%">
          <stop offset="0%" stop-color="#2fa3dc"/>
          <stop offset="45%" stop-color="#9bc84a"/>
          <stop offset="75%" stop-color="#a88fc8"/>
          <stop offset="100%" stop-color="#ffffff" stop-opacity="0"/>
        </radialGradient>
      </defs>
      <rect class="tree-illustration" x="560" y="30" width="410" height="420" rx="200"
            fill="url(#canopy)" opacity="0.55" role="img"
            aria-label="Multicoloured tree with red, blue, green, purple and yellow leaves growing from an open hand"/>
      <path class="hill-navy" d="M250 571 C 420 420, 800 390, 1000 440 L1000 571 Z" fill="var(--navy)"/>
      <path class="hill-green" d="M370 571 C 520 470, 800 445, 1000 470 L1000 571 Z" fill="var(--green)"/>
      <text class="tagline" x="880" y="508" text-anchor="end" font-family="Arimo, sans-serif" font-size="24" fill="#fff">Para un</text>
      <text class="tagline" x="900" y="542" text-anchor="end" font-family="Arimo, sans-serif" font-size="27" font-weight="700" fill="#fff">futuro mas seguro!</text>
    </svg>

    <div class="brand">
      <span class="brand-dot"></span>
      <span class="brand-name">Valemar</span>
    </div>

    <div class="holder">Anselmo Ibarra <span class="suffix">Jr</span></div>

    <ul class="contact-list">
      <li>
        <svg viewBox="0 0 24 24"><path d="M6.6 10.8a15 15 0 0 0 6.6 6.6l2.2-2.2a1 1 0 0 1 1-.25 11.4 11.4 0 0 0 3.6.6 1 1 0 0 1 1 1V20a1 1 0 0 1-1 1A17 17 0 0 1 3 4a1 1 0 0 1 1-1h3.5a1 1 0 0 1 1 1c0 1.25.2 2.45.57 3.57a1 1 0 0 1-.25 1Z" fill="var(--green)"/></svg>
        951-555-0147
      </li>
      <li>
        <svg viewBox="0 0 24 24"><rect x="2.5" y="5" width="19" height="14" fill="none" stroke="var(--green)" stroke-width="2"/><path d="M2.5 5l9.5 8 9.5-8" fill="none" stroke="var(--green)" stroke-width="2"/></svg>
        info@celestafinancialgroup.example
      </li>
      <li>
        <svg viewBox="0 0 24 24"><circle cx="12" cy="12" r="9.5" fill="none" stroke="var(--green)" stroke-width="2"/><path d="M2.5 12h19M12 2.5c3 3 3 16 0 19M12 2.5c-3 3-3 16 0 19" fill="none" stroke="var(--green)" stroke-width="1.6"/></svg>
        Celestafinancialgroup.example
      </li>
    </ul>
  </div>
</body>
</html>
```